New Premium Rum

We need label for an exclusive rum named after our family name. Ron Valcastro. This rum sells for 50 US and is aged at least 10 years. There is a lot of tradition involved. This rum is from Belize, Central America.
My website is www.quietcovedistill.com if you want to check some of our other products.

Reason: I would like to get more designs to view and have more time to give feedback.

Reason: I did not get designs I really like

```html
<!DOCTYPE html>
<html lang="en">
<head>
<meta charset="UTF-8">
<title>Ron Valcastro – Rum Label</title>
<link rel="stylesheet" href="https://fonts.googleapis.com/css2?family=Open+Sans:wght@400;600&display=swap">
<style>
  :root {
    --page: #ffffff;
    --label-gold: #e2a01e;
    --band-maroon: #960029;
    --name-maroon: #74152f;
    --glyph-tone: #b8561f;
  }
  html, body {
    margin: 0;
    padding: 0;
    width: 1200px;
    height: 1200px;
    overflow: hidden;
    background: var(--page);
  }
  .canvas {
    display: block;
    width: 1200px;
    height: 1200px;
  }
  .label-base { fill: var(--label-gold); }
  .top-band { fill: var(--band-maroon); }
  .name-panel { fill: var(--label-gold); }
  .glyph-area { fill: var(--glyph-tone); }
  .origin-text,
  .age-text {
    font-family: "Open Sans", sans-serif;
    font-weight: 400;
    fill: var(--label-gold);
  }
  .origin-text { font-size: 18.5px; }
  .age-text { font-size: 24px; letter-spacing: 0.5px; }
  .product-name {
    font-family: "Open Sans", sans-serif;
    font-weight: 600;
    font-size: 70px;
    fill: var(--name-maroon);
  }
</style>
</head>
<body>
<svg class="canvas" viewBox="0 0 1200 1200" xmlns="http://www.w3.org/2000/svg">
  <rect class="label-base" x="261" y="345" width="700" height="441"/>

  <path class="top-band" d="M297 392 H933 V712 Q933 750 895 750 H335 Q297 750 297 712 Z"/>

  <rect class="glyph-area" x="567" y="405" width="93" height="141" rx="8"
        role="img" aria-label="Mayan glyph illustration"/>

  <text class="origin-text" text-anchor="middle">
    <tspan x="441" y="515">IMPORTED FROM</tspan>
    <tspan x="441" y="537">Belize, Central America</tspan>
  </text>

  <text class="age-text" text-anchor="middle">
    <tspan x="783" y="510">10 YEAR OLD</tspan>
    <tspan x="783" y="538">GOLD RUM</tspan>
  </text>

  <path class="name-panel" d="M309 564 H921 V715 Q921 738 898 738 H332 Q309 738 309 715 Z"/>

  <text class="product-name" x="615" y="677" text-anchor="middle">Ron Valcastro</text>
</svg>
</body>
</html>
```